Capability statement for an Electrical Business based in Sydney Australia

The aim for the Capability statement is for us to look more professional when we meet someone or after cold calling and have to send them our business details.
Need something simple, efficient and to the point.

It should have the following content
- Our mission (details can be as attached PDF)
- Areas we service (this can be a google map of areas we service but basically the areas are
Metro Sydney with our work centralised around the Norwest, Hills, Inner west and Epping area)
- List of services we provide (as PDF)
- Details about us; who we are, contact details, licenses (as PDF)
- Why they should choose us
(As pdf)

Right now, we're just after a nice format we're happy with, the details we are happy to provide with once we have a design in mind.

I've attached our current existing capability statement and what our details are. Also, our website is
https://themardenfield.com.au/

Thanks in advance!

• Should not be complicated for the reader

```html
<!DOCTYPE html>
<html lang="en">
<head>
<meta charset="utf-8">
<title>The Marden Field – Capability Statement</title>
<link rel="stylesheet" href="https://fonts.googleapis.com/css2?family=Lato:ital,wght@0,400;0,700;0,900;1,400&display=swap">
<style>
  :root {
    --backdrop: #3a3a3a;
    --red: #d82a27;
    --black: #000000;
    --white: #ffffff;
    --stripe: #222222;
    --ceiling-light: #f4f2f4;
    --ceiling-mid: #cfc8cf;
    --wall-warm: #b58c6e;
  }
  * { margin: 0; padding: 0; box-sizing: border-box; }
  html, body { width: 1200px; height: 1200px; overflow: hidden; }
  body {
    background: var(--backdrop);
    font-family: "Lato", sans-serif;
    color: var(--white);
    position: relative;
  }
  .sheet {
    position: absolute; left: 204px; top: 40px;
    width: 792px; height: 1120px;
    background: var(--black);
    overflow: hidden;
  }
  .hero {
    position: absolute; left: 0; top: 0; width: 792px; height: 214px;
    background: linear-gradient(100deg, var(--ceiling-light) 0%, var(--ceiling-light) 35%, var(--ceiling-mid) 60%, #d8cbc6 80%, var(--wall-warm) 100%);
  }
  .hero-slash { position: absolute; left: 0; top: 0; }
  .brand {
    position: absolute; left: 36px; top: 58px;
    display: flex; align-items: center; gap: 9px;
    color: var(--red); font-weight: 900; font-size: 24px; letter-spacing: 0.5px;
    line-height: 1; white-space: nowrap;
  }
  .brand-mark { width: 12px; height: 12px; background: var(--red); }
  .title-band {
    position: absolute; left: 409px; top: 29px; width: 383px; height: 54px;
    background: var(--red);
    clip-path: polygon(20px 0, 100% 0, 100% 100%, 0 100%);
    display: flex; align-items: center; padding-left: 38px;
    font-size: 27px; font-weight: 700; white-space: nowrap;
  }
  .right-panel {
    position: absolute; left: 387px; top: 198px; width: 405px; height: 912px;
    background: var(--red);
  }
  .footer-left { position: absolute; left: 0; top: 1110px; width: 387px; height: 10px; background: var(--red); }
  .tab {
    position: absolute; height: 31px;
    display: flex; align-items: center; justify-content: center;
    font-size: 15px; font-weight: 700; white-space: nowrap;
  }
  .tab-red { background: var(--red); border-radius: 16px 0 0 16px; left: 32px; width: 355px; }
  .tab-black { background: var(--black); border-radius: 0 16px 16px 0; left: 387px; width: 371px; }
  .block {
    position: absolute; font-size: 15px; line-height: 17.6px; letter-spacing: -0.2px;
  }
  .block h3 { font-size: 15px; font-weight: 700; }
  .values { list-style: none; font-style: italic; margin-top: 9px; }
  .values li, .services li { position: relative; padding-left: 24px; }
  .values li::before, .services li::before {
    content: ""; position: absolute; left: 2px; top: 7px;
    width: 5px; height: 5px; border-radius: 50%; background: var(--white);
  }
  .services { list-style: none; }
  .map-area {
    position: absolute; left: 44px; top: 488px; width: 322px; height: 290px;
    background: linear-gradient(120deg, #b4dfe0 0%, #b4dfe0 22%, #f6cf8f 30%, #f3ead7 50%, #eee3cf 75%, #cfe2b8 100%);
  }
  .contact b { font-weight: 700; }
</style>
</head>
<body>
  <main class="sheet">
    <section class="hero" role="img" aria-label="Photo of a modern interior ceiling with downlights and white pendant lamps"></section>
    <svg class="hero-slash" width="792" height="214" viewBox="0 0 792 214" aria-hidden="true">
      <polygon points="373,0 440,0 360,162 290,162" fill="#222"/>
      <rect x="0" y="198" width="792" height="16" fill="#d82a27"/>
    </svg>

    <div class="brand"><span class="brand-mark"></span>THE MARDEN FIELD</div>
    <div class="title-band">CAPABILITY STATEMENT</div>

    <div class="right-panel"></div>
    <div class="footer-left"></div>

    <div class="tab tab-red" style="top:198px;">OUR MISSION</div>
    <div class="block" style="left:44px; top:243px; width:335px;">
      <p>Dedicate ourselves to providing world class service to anyone in need, based on honesty, communication and respect.</p>
      <h3 style="margin-top:8px;">CORE VALUES</h3>
      <ul class="values">
        <li>Safety and Security is priority</li>
        <li>Support when you need it most</li>
        <li>Service with an over-the-top WOW</li>
        <li>Satisfaction with loyalty and integrity</li>
      </ul>
    </div>

    <div class="tab tab-red" style="top:402px;">AREAS WE SERVICE</div>
    <div class="block" style="left:44px; top:450px; width:335px;">
      <p>Metro Sydney with our work centralised around the Norwest, Hills, Inner west and Epping area</p>
    </div>
    <div class="map-area" role="img" aria-label="Map of the service area around Metro Sydney"></div>

    <div class="tab tab-red" style="top:797px;">THE MOST COMMON SERVICES WE PROVIDE</div>
    <div class="block" style="left:44px; top:848px; width:342px;">
      <ul class="services">
        <li>24/7 Emergency service</li>
        <li>Switchboard UPGRADE and REPAIRS</li>
        <li>Light fitting installations</li>
        <li>Powerpoint installations</li>
        <li>Surge device installations</li>
        <li>Testing and servicing electric hot water systems</li>
        <li>Smoke Alarm installation with compliance</li>
        <li>certificate</li>
        <li>Electric Vehicle charging stations</li>
        <li>Ceiling and Exhaust fan installations with roof and wall venting</li>
        <li>Appliance installations</li>
        <li>Fault finding</li>
        <li>TV, DATA and FREE TO AIR Aerial installations</li>
      </ul>
    </div>

    <div class="tab tab-black" style="top:230px;">WHO WE ARE</div>
    <div class="block" style="left:417px; top:281px; width:352px;">
      <p>The Marden Field is a growing Electrical maintenance company based in the Inner West.</p>
      <p>We are established on sound service principles with honesty, communication, and respect at the forefront of every team member.</p>
      <p>We strive for openness, trust, and accountability and we are in the business of providing solutions to help others. We see ourselves as part of your team.</p>
    </div>

    <div class="tab tab-black" style="top:433px;">WHY CHOOSE THE MARDEN FIELD</div>
    <div class="block" style="left:417px; top:482px; width:355px;">
      <h3>SUPPORT WHEN YOU NEED IT MOST</h3>
      <p>The Field provides around the clock assistance, whether during normal business hours or emergencies we are focused on providing solutions for our clients.</p>
      <h3>FAST AND RESPONSIVE TEAM WITH A DIRECT CONTACT</h3>
      <p>The Field treats every one of our clients as a VIP. We pride ourselves on being able to provide a quick turn around for all our jobs. We make the whole process smooth, from booking the job to attending and completion.</p>
      <h3>SATISFACTION WITH LOYALTY AND INTEGRITY</h3>
      <p>We value our transparency and communication skills to deliver an outstanding performance which reflects our happy customer base.</p>
      <h3>WE PROVIDE COURTESY CALLS</h3>
      <p>The appointment will be confirmed the day before and our technicians will call you half an hour in advance on approach to the job</p>
      <h3>Licensed and insured technicians</h3>
      <p>All our technicians are experts of their field, with the relevant equipment, knowledge and licenses to carry out our duties.</p>
    </div>

    <div class="tab tab-black" style="top:903px;">CONTACT AND LICENSES</div>
    <div class="block contact" style="left:418px; top:953px; width:355px;">
      <p><b>Email :</b> Services@themardenfield.com.au</p>
      <p><b>Mobile Phone :</b></p>
      <p>Daniel - 0412 555 018</p>
      <p>Bradley - 0498555027</p>
      <p><b>Electrical license number :</b></p>
      <p>The Marden Field Pty Ltd - 518207C</p>
      <p>Daniel - 264731C</p>
      <p>Bradley - 379152C ABN: 5102 8843 619</p>
      <p><b>Public Liability :</b> $20,000,000</p>
    </div>
  </main>
</body>
</html>
```